Advertising Agencies

I am a consumer product contract manufacturing and packaging consultant. I service the following industries: food, nutritional supplements, hair care, skin care, cosmetics and electronics. I serve as a 3rd party supply chain management solution so that my customers can focus on selling their product and growing their business vs. dealing with the actual manufacturing & packaging of their product. Advertising agencies are often contacted in the early stages of product design. During this early stage is an ideal time for us to take a look at the product, manufacturing & packaging and provide feedback on feasibility, cost, lead times, etc. We need a postcard that encourages the production manager at the advertising agency to include us (at no cost) at the 'round table' early in the product design stages.

Per the attached clip art: I'm envisioning something like this, eye catching, that depicts the various people at the board room meeting: The consumer product company owner, the ad firm designer, the ad firm PR/marketing person and myself the manufacturing & packaging consultant. Perhaps centered on the table will be a 2oz all natural shot drink with a shrink sleeve on it & inside its display box.

Websites:
Brindlemarkcrest.com
TorvaPak.com
7QRTN.site.mobi - Tablet or smartphone mobile site
Some copy that could be used on the card: http://www.wrapfolio.example/contract-packaging/strategy/why-contract-packagers-need-be-involved-early-product-development-cycle

```html
<!DOCTYPE html>
<html lang="en">
<head>
<meta charset="utf-8">
<title>TorvaPak Postcard</title>
<link rel="stylesheet" href="https://fonts.googleapis.com/css2?family=Oswald:wght@500;600&family=Lato:wght@400;700;900&family=Arimo:wght@400;700&display=swap">
<style>
  :root {
    --stage: #2a2826;
    --blue: #1d9ad6;
    --blue-deep: #0f79b4;
    --blue-light: #3fb6e6;
    --ink: #333333;
    --gray-dark: #2e2e30;
    --gray-mid: #545457;
    --white: #ffffff;
    --red: #e0242c;
  }
  * { box-sizing: border-box; margin: 0; padding: 0; }
  html, body { width: 806px; height: 1200px; overflow: hidden; }
  body { background: var(--stage); position: relative; font-family: "Arimo", Arial, sans-serif; }

  .card { position: absolute; background: var(--white); overflow: hidden; }
  .card-front { left: 72px; top: 64px; width: 660px; height: 512px; }
  .card-back { left: 70px; top: 616px; width: 662px; height: 512px; }
  .card-shapes { position: absolute; inset: 0; }

  /* Front */
  .meeting-art {
    position: absolute; left: 20px; top: 14px; width: 290px; height: 240px;
    background: radial-gradient(ellipse at 55% 60%, #9fd0ec 0%, #cfe7f5 55%, #ffffff 100%);
  }
  .feedback-board {
    position: absolute; left: 24px; top: 20px; width: 140px; height: 76px;
    background: #111; border: 2px solid #444;
    color: var(--red); font: 700 13.5px/1.2 "Arimo", Arial, sans-serif; text-align: center;
    padding-top: 12px;
  }
  .front-headline {
    position: absolute; right: 16px; top: 30px; width: 440px; text-align: right;
    color: var(--blue); font: 600 16.5px/1.32 "Oswald", "Arial Narrow", sans-serif; letter-spacing: 0.3px;
  }
  .front-intro {
    position: absolute; right: 18px; top: 82px; width: 318px; text-align: right;
    color: var(--ink); font: 700 9.3px/1.42 "Arimo", Arial, sans-serif;
  }
  .benefits {
    position: absolute; left: 470px; top: 200px; width: 170px; color: var(--white);
  }
  .benefits-title { font: 600 25px/1.0 "Oswald", "Arial Narrow", sans-serif; letter-spacing: 0.3px; margin-bottom: 8px; }
  .benefits-list { list-style: none; font: 400 8.8px/1.15 "Arimo", Arial, sans-serif; }
  .benefits-list li { position: relative; padding-left: 9px; margin-bottom: 4px; }
  .benefits-list li::before { content: "●"; position: absolute; left: 0; top: 1px; font-size: 7.5px; }
  .benefits-list strong { font-size: 10.5px; font-weight: 700; }

  .services { position: absolute; left: 18px; top: 344px; width: 628px; color: var(--white); font: 700 9.3px/1.45 "Arimo", Arial, sans-serif; }
  .service { margin-bottom: 3px; }
  .service-narrow { width: 438px; }
  .service-title { color: var(--blue-light); font: 500 19px/1 "Oswald", "Arial Narrow", sans-serif; margin-right: 4px; }
  .service-title::before { content: "❯"; font-size: 15px; margin-right: 2px; }

  /* Back */
  .back-panel {
    position: absolute; left: 0; top: 0; width: 305px; height: 400px;
    background: linear-gradient(180deg, #1b95d1 0%, #26a8e0 60%, #1d9ad6 100%);
    padding: 16px 16px 0 16px; color: var(--white);
  }
  .back-headline { font: 900 15.5px/1.2 "Lato", Arial, sans-serif; margin-bottom: 10px; }
  .back-copy { font: 700 9px/1.45 "Lato", Arial, sans-serif; margin-bottom: 7px; }
  .product-art {
    position: absolute; left: 40px; top: 242px; width: 250px; height: 142px;
    background: linear-gradient(135deg, #c9a27a 0%, #c8323a 40%, #3a3a3a 65%, #6fc6e8 100%);
    opacity: 0.9;
  }
  .stamp-box { position: absolute; left: 530px; top: 41px; width: 83px; height: 83px; border: 1.5px solid #222; }
  .address-line { position: absolute; left: 320px; width: 327px; height: 0; border-top: 1.5px solid #222; }
  .sender {
    position: absolute; right: 16px; top: 392px; text-align: right; font-style: normal;
    color: var(--white); font-weight: 400; font-size: 16.5px; line-height: 1.36; font-family: "Lato", Arial, sans-serif;
  }
  .contact-row {
    position: absolute; right: 16px; top: 460px; display: flex; align-items: center; gap: 6px;
    color: var(--white); font: 400 15px/1 "Lato", Arial, sans-serif;
  }
  .phone { color: var(--blue-light); font: 600 19px/1 "Oswald", "Arial Narrow", sans-serif; margin-left: 6px; }
</style>
</head>
<body>

<section class="card card-front">
  <svg class="card-shapes" width="660" height="512" viewBox="0 0 660 512" aria-hidden="true">
    <defs>
      <linearGradient id="frontGray" x1="0" y1="0" x2="0" y2="1">
        <stop offset="0" stop-color="#5a5a5d"/>
        <stop offset="1" stop-color="#2b2b2d"/>
      </linearGradient>
    </defs>
    <polygon points="0,268 230,318 660,170 660,512 0,512" fill="url(#frontGray)"/>
    <polygon points="0,232 232,286 660,140 660,162 232,300 0,252" fill="#1d9ad6"/>
    <polygon points="0,252 232,300 660,162 660,170 230,318 0,268" fill="#ffffff"/>
    <path d="M484 160 L632 150 Q645 150 645 164 L645 384 Q645 398 631 398 L474 398 Q460 398 460 384 L460 190 Q460 170 484 160 Z" fill="#1d9ad6"/>
    <polygon points="0,488 300,476 660,464 660,472 300,484 0,496" fill="#ffffff"/>
    <polygon points="0,496 300,484 660,472 660,512 0,512" fill="#1d9ad6"/>
  </svg>

  <div class="meeting-art" role="img" aria-label="Illustration of figures seated around a boardroom table with a presenter and packaged product samples on the table"></div>
  <div class="feedback-board">Early Packaging<br>Feedback = Time<br>&amp; Cost Savings</div>

  <h1 class="front-headline">WHY CONTRACT PACKAGERS NEED TO BE INVOLVED EARLY<br>IN THE PRODUCT DEVELOPMENT CYCLE</h1>
  <p class="front-intro">Of the few leading brand owners who do include contract packers early in the product development cycle, a practice which is becoming more common, they have reaped significant rewards the biggest of which being cited as cost &amp; time savings.</p>

  <aside class="benefits">
    <h2 class="benefits-title">BRAND OWNER<br>BENEFITS</h2>
    <ul class="benefits-list">
      <li><strong>COST SAVINGS:</strong> Most cost effective manufacturing process</li>
      <li><strong>TIME SAVINGS:</strong> Increased speed to market</li>
      <li><strong>OPTIMAL DESIGN:</strong> Product enhancement recommendations</li>
      <li><strong>SUPPLIER RELATIONSHIP:</strong> Improved operations &amp; collaboration</li>
    </ul>
  </aside>

  <div class="services">
    <p class="service service-narrow"><span class="service-title">ABOUT US</span> We are a leading provider of turn-key contract manufacturing,packaging and warehousing/fulfillment. Industries that we service include Electronics, Nutritional Supplements, Food &amp; Beverage,Cosmetics, Hair Care &amp; Skin Care.</p>
    <p class="service service-narrow"><span class="service-title">PRINTING</span> simple print, complicated catalogs, labels, shrink sleeves;</p>
    <p class="service"><span class="service-title">BOXES</span> folding cartons, POP displays, corrugated; Packaging - single serving sample packets, stick packs, pouches, tubes, jars, bottles,canisters - we provide both the components as well as the filling. We can fill liquids, powders, gels, lotions, oils, creams, tablets,capsules and softgels into packets, stick packs, tubes, bottles, jars and canisters.</p>
  </div>
</section>

<section class="card card-back">
  <svg class="card-shapes" width="662" height="512" viewBox="0 0 662 512" aria-hidden="true">
    <defs>
      <linearGradient id="backGray" x1="0" y1="0" x2="0" y2="1">
        <stop offset="0" stop-color="#5a5a5d"/>
        <stop offset="1" stop-color="#2b2b2d"/>
      </linearGradient>
    </defs>
    <polygon points="0,408 305,408 662,262 662,512 0,512" fill="url(#backGray)"/>
  </svg>

  <div class="back-panel">
    <h2 class="back-headline">Wrapfolio Review is the leading business resource for today's packaging professionals.</h2>
    <p class="back-copy">The most experienced journalists in packaging and unparalleled reach into the marketplace have made Wrapfolio Review the number one media choice of companies who sell to the $500+ billion packaging industry.</p>
    <p class="back-copy">Each month, we deliver a total reach of over 125,000 professionals, across our magazine, website, and apps, as verified by our Audit Circle Brand Report. We offer additional exposure for marketers via digital ad products and our growing social media influence, reaching professionals in food, beverage, pharmaceuticals, consumer products and all package-using industries.</p>
  </div>
  <div class="product-art" role="img" aria-label="Collage of packaging samples: magazine cover, bags, sachets, boxes and stick packs"></div>

  <div class="stamp-box"></div>
  <div class="address-line" style="top:164px"></div>
  <div class="address-line" style="top:187px"></div>
  <div class="address-line" style="top:214px"></div>

  <address class="sender">TorvaPak I BMC<br>2210 W. Harlow Ave.<br>Fullerton, CA 92833</address>

  <div class="contact-row">
    <svg width="14" height="14" viewBox="0 0 14 14" aria-hidden="true">
      <g fill="none" stroke="#fff" stroke-width="1.1">
        <circle cx="7" cy="7" r="6"/><ellipse cx="7" cy="7" rx="2.6" ry="6"/><line x1="1" y1="7" x2="13" y2="7"/>
      </g>
    </svg>
    <span>TorvaPak.com</span>
    <svg width="18" height="18" viewBox="0 0 18 18" aria-hidden="true" style="margin-left:8px">
      <rect width="18" height="18" rx="3" fill="#3fb6e6"/>
      <path d="M5 4 L7.5 4 L8.5 7 L7 8 Q8 10.5 10 11 L11 9.5 L14 10.5 L14 13 Q13 14 11 14 Q5 12.5 4 6 Q4 4.5 5 4 Z" fill="#2e2e30"/>
    </svg>
    <span class="phone">480-555-0147</span>
  </div>
</section>

</body>
</html>
```